Blue Harbor Business Cards

Name Tomas Welbridge
Title Mortgage Originator
Phone (800) 614-2290 x32
Direct (571) 362-0471
Email twelbridge@blueharborhomeloans.com
NMLS #1847362
Name Lena Ortiz
Title Mortgage Originator
Location (800) 614-2290 x55
Direct (440) 276-5190
Email lortiz@blueharborhomeloans.com
NMLS #2739418
Name Desmond Holloway-Finch
Title Mortgage Originator
Location (800) 614-2290 x56
Direct (202) 634-1975
Email dhollowayfinch@blueharborhomeloans.com
NMLS #2784530
Name Rosalyn Whitaker
Title Mortgage Originator
Location (800) 614-2290 x57
Direct (240) 358-6621
Email rwhitaker@blueharborhomeloans.com
NMLS #2491086
Name Gwen Holbrook
Title Mortgage Originator
Location (800) 614-2290 x58
Direct (540) 716-2384
Email gholbrook@blueharborhomeloans.com
NMLS #2438617
Name Ravi Dunmore
Title Mortgage Originator
Location (800) 614-2290 x59
Direct (240) 563-8827
Email rdunmore@blueharborhomeloans.com
NMLS #2597142
Name Ivy Marlow
Title Mortgage Originator
Location (800) 614-2290 x60
Direct (202) 479-3306
Email ivy@ivyfindshomes.com
NMLS #2718394
Contact Information for Business Card
Name Tomas Welbridge Title Mortgage Originator Phone (800) 614-2290 x32 Direct (571) 362-0471 Email twelbridge@blueharborhomeloans.com NMLS #1847362 Name Lena Ortiz Title Mortgage Originator Location (800) 614-2290 x55 Direct (440) 276-5190 Email lortiz@blueharborhomeloans.com NMLS #2739418 Name Desmond Holloway-Finch Title Mortgage Originator Location (800) 614-2290 x56 Direct (202) 634-1975 Email dhollowayfinch@blueharborhomeloans.com NMLS #2784530 Name Rosalyn Whitaker Title Mortgage Originator Location (800) 614-2290 x57 Direct (240) 358-6621 Email rwhitaker@blueharborhomeloans.com NMLS #2491086 Name Gwen Holbrook Title Mortgage Originator Location (800) 614-2290 x58 Direct (540) 716-2384 Email gholbrook@blueharborhomeloans.com NMLS #2438617 Name Ravi Dunmore Title Mortgage Originator Location (800) 614-2290 x59 Direct (240) 563-8827 Email rdunmore@blueharborhomeloans.com NMLS #2597142 Name Ivy Marlow Title Mortgage Originator Location (800) 614-2290 x60 Direct (202) 479-3306 Email ivy@ivyfindshomes.com NMLS #2718394
Look and feel
Each slider illustrates characteristics of the customer's brand and the style your logo design should communicate.

```html
<!DOCTYPE html>
<html lang="en">
<head>
<meta charset="utf-8">
<title>Blue Harbor – Desmond Holloway-Finch Business Card</title>
<link rel="stylesheet" href="https://fonts.googleapis.com/css2?family=Archivo:wght@300;400;500;700;800&family=Montserrat:wght@700;800&display=swap">
<style>
  :root {
    --wine: #581f37;
    --paper: #fafcfb;
    --ink: #2f2f33;
    --muted: #9c9c9c;
    --backdrop-top: #e6e6e6;
    --backdrop-bottom: #d2d2d2;
    --photo-light: #b9a9a6;
    --photo-dark: #4a2a30;
  }
  * { box-sizing: border-box; margin: 0; padding: 0; }
  html, body { width: 999px; height: 1200px; overflow: hidden; }
  body {
    position: relative;
    background: linear-gradient(180deg, var(--backdrop-top), var(--backdrop-bottom));
    font-family: "Archivo", Arial, sans-serif;
  }
  .card {
    position: absolute;
    left: 108px;
    width: 782px;
    height: 447px;
    border-radius: 57px;
    overflow: hidden;
    box-shadow: 0 22px 30px rgba(0,0,0,0.16);
  }
  .card-front { top: 82px; background: var(--paper); }
  .card-back { top: 671px; background: var(--wine); }

  .side-panel {
    position: absolute; left: 580px; top: 0; width: 202px; height: 100%;
    background: var(--wine);
  }
  .name {
    position: absolute; left: 48px; top: 78px;
    font-size: 33px; line-height: 1; color: var(--wine);
    letter-spacing: 0.3px; white-space: nowrap;
  }
  .name .first { font-weight: 300; }
  .name .last { font-weight: 700; }
  .title {
    position: absolute; left: 52px; top: 112px;
    font-size: 18px; font-weight: 500; color: var(--muted);
  }
  .nmls-bar {
    position: absolute; left: 0; top: 151px; width: 310px; height: 29px;
    background: var(--wine); color: #fff;
    padding-left: 51px; font-size: 18px; line-height: 29px; letter-spacing: 0.6px;
  }
  .nmls-bar strong { font-weight: 700; letter-spacing: 1px; }

  .contacts { position: absolute; left: 52px; top: 296px; list-style: none; }
  .contacts li {
    display: flex; align-items: center; height: 32.5px;
    font-size: 18px; color: var(--ink); letter-spacing: 0.4px;
  }
  .contacts svg { width: 18px; height: 18px; margin-right: 19px; flex: none; }

  .portrait { position: absolute; left: 496px; top: 136px; width: 174px; height: 174px; }

  .divider {
    position: absolute; left: 257px; top: 118px; width: 3px; height: 209px; background: #fff;
  }
  .brand { position: absolute; left: 282px; top: 200px; color: #fff; font-family: "Montserrat", Arial, sans-serif; }
  .brand-name { font-size: 27px; font-weight: 800; letter-spacing: 1px; line-height: 1; }
  .brand-slogan { font-size: 15px; font-weight: 800; letter-spacing: 6.5px; margin-top: 4px; }
</style>
</head>
<body>
  <section class="card card-front">
    <div class="side-panel"></div>
    <h1 class="name"><span class="first">DESMOND </span><span class="last">HOLLOWAY-FINCH</span></h1>
    <p class="title">Mortgage Originator</p>
    <div class="nmls-bar">NMLS <strong>#2784530</strong></div>

    <ul class="contacts">
      <li>
        <svg viewBox="0 0 18 18"><circle cx="9" cy="9" r="9" fill="var(--wine)"/><path d="M6.2 4.6l1.4 1.9-.8 1.1c.6 1.3 1.5 2.2 2.8 2.8l1.1-.8 1.9 1.4-.8 1.6c-3.6-.3-6.9-3.6-7.2-7.2z" fill="#fff"/></svg>
        (800) 614-2290 x56
      </li>
      <li>
        <svg viewBox="0 0 18 18"><circle cx="9" cy="9" r="9" fill="var(--wine)"/><rect x="6" y="4" width="6" height="10" rx="1.2" fill="#fff"/><rect x="7.1" y="5.3" width="3.8" height="6.6" fill="var(--wine)"/></svg>
        (202) 634-1975
      </li>
      <li>
        <svg viewBox="0 0 18 18"><circle cx="9" cy="9" r="9" fill="var(--wine)"/><rect x="4.8" y="6" width="8.4" height="6" rx="0.6" fill="#fff"/><path d="M4.9 6.3L9 9.3l4.1-3" fill="none" stroke="var(--wine)" stroke-width="1"/></svg>
        dhollowayfinch@blueharborhomeloans.com
      </li>
    </ul>

    <svg class="portrait" viewBox="0 0 174 174">
      <defs>
        <linearGradient id="portrait-tone" x1="0" y1="0" x2="0" y2="1">
          <stop offset="0" stop-color="var(--photo-light)"/>
          <stop offset="1" stop-color="var(--photo-dark)"/>
        </linearGradient>
      </defs>
      <circle cx="87" cy="87" r="87" fill="#fff"/>
      <circle cx="87" cy="87" r="82" fill="none" stroke="var(--wine)" stroke-width="3.5"/>
      <circle cx="87" cy="87" r="76" fill="url(#portrait-tone)" role="img" aria-label="Headshot of Desmond Holloway-Finch"/>
    </svg>
  </section>

  <section class="card card-back">
    <div class="divider"></div>
    <div class="brand">
      <div class="brand-name">BUSINESS LOGO</div>
      <div class="brand-slogan">SLOGAN</div>
    </div>
  </section>
</body>
</html>
```